Creative Realtor Business Card Design

I need a creative business card.... I would like it to be larger than the normal size...heavy stock.... colorful...
As you are probably aware, there are tons of realtors, and most of their cards ALL look alike.. potential clients are looking for agents that are professional, but are different.
Cards are a form of advertising and I need your help to make mine stand out in a professional, classy way.
I don't need to use the ridgeway meadow realty logo, my personal logo is MORE important for branding purposes. OR..what is your opinion?
YOU DESIGN FOR ME PLEASE! If I could do what you do I would.... I can't and I need your professional help.

                                        If you think I need the card to be double sided so it doesn't look busy by all means I will happily accept double sided. 

I am very interested in a more "creative" card than a standard run of the mill realtor card.    I care about my clients LONG after the sale has closed!

                                   

THANK YOU SO MUCH FOR YOUR EFFORTS AND TALENTS....I APPRECIATE IT SO MUCH! 

                                        Would it be possible to use my theme of my logo to design my card?

                                            Where Every Doorstep Feels Familiar

                              

 

Please make cards larger size .... See this link for ideas that appeal to me. Thank you for your interest.

https://www.lookfindery.example/search?q=examples+of+unique+business+cards&mode=img&ref=7QpLm2VxT9kAzR4bWcYnHe&pg=1

I want my card to stand out in size and design...

Thank you so much for your hard work for me.

Lorna

 

Reason: I learned that many designers are very busy. I am providing more time and money in hopes that designers will find it an attractive enough challenge to participate. My business cards are one of my most important marketing materials...I NEED THEM TO BE DISTINCTIVE, CLASSY, and INFORMATIVE. Thank you SO MUCH....and I will be anxiously awaiting your great designs... Lorna

Hello Designers,

Thank you to all you creative people that have kindly offered to submit your creative design(s) for my business card.  I view your designs as your creative artwork. I am anxious to see where your creativity leads you.

I wanted to share with you that my logo was something I personally designed after being in business for 3  years. ( I did have to have a professionals like yourselves draw it for me). The design and logo captured perfectly how I felt about my work ...helping individuals, such as you, find a home.  A house is easy to find, but a home is a place that has "good" energy ... a place where you feel comfortable and can grow.  A place that just "Feels right!"  It's one of those things that you just KNOW when it is right! 

I hope by sharing this bit of information about me can help you creatively design my card for me...I care for my clients LONG after the transaction has closed and they are in their home. Thank you again for taking the time to work on my design. I have been adding money so that your time spent on my card is worth it.

I do need my card soon...so please, if you have a design...submit it!

Kind Regards,

Lorna

Target Market(s)

I have a variety of clients from a mobile home of $35,000 to an estate property for $5M. I feel comfortable working with all types of people...I love my job...I love helping people find the right home because we all know how our home environment affects our well being.

Industry/Entity Type

Advertising

Contact Information for Business Card

Lorna Packett, Realtor
Ridgeway Meadow Realty
"Where Every Doorstep Feels Familiar"
www.lornaplaces.example
lpackett@mailbrook.example
(555) 418-6032
BRE #04782915, Exp. 8/15

Colors

Designer to choose colors to be used in the design.

Requirements
Must have
• By law, my license number information MUST be on my card.
Nice to have
• I would love card to be memorable...if that is possible for a business card. Also, I would like my card to be larger than the average card. Not sure that is possible either.

```html
<!DOCTYPE html>
<html lang="en">
<head>
<meta charset="utf-8">
<title>Lorna Packett, Realtor – Business Card</title>
<link rel="stylesheet" href="https://fonts.googleapis.com/css2?family=Oswald:wght@400;500&display=swap">
<style>
  :root {
    --purple: #8b4a9f;
    --purple-deep: #7a3c8f;
    --purple-text: #8d49a1;
    --yellow: #f3cf40;
    --ink: #262626;
    --white: #ffffff;
  }
  * { margin: 0; padding: 0; box-sizing: border-box; }
  html, body { width: 1200px; height: 702px; overflow: hidden; background: var(--purple); }
  .card {
    position: relative;
    width: 1200px;
    height: 702px;
    overflow: hidden;
    background: var(--purple);
    font-family: "Oswald", "Arial Narrow", sans-serif;
  }
  .house-photo {
    position: absolute;
    left: 230px; top: 0;
    width: 720px; height: 600px;
    background:
      radial-gradient(ellipse 60% 55% at 50% 40%, rgba(196,110,190,0.55), rgba(139,74,159,0) 70%),
      linear-gradient(180deg, #9a5aa8 0%, #7d4290 55%, rgba(139,74,159,0) 100%);
  }
  .accent-wedge { position: absolute; inset: 0; }
  .identity { position: absolute; left: 59px; top: 58px; }
  .identity span {
    display: block;
    width: max-content;
    font-size: 86px;
    line-height: 88px;
    text-transform: uppercase;
    letter-spacing: 0.5px;
    padding: 0 18px 0 10px;
  }
  .identity .name { background: var(--white); color: var(--ink); }
  .identity .title { background: var(--ink); color: var(--white); }
  .contacts { position: absolute; left: 59px; top: 279px; list-style: none; }
  .contact { position: relative; height: 88px; margin-bottom: 22px; display: flex; align-items: center; }
  .contact .badge {
    position: relative; z-index: 2;
    width: 88px; height: 88px; border-radius: 50%;
    background: var(--white); color: var(--ink);
    display: flex; align-items: center; justify-content: center;
    font-size: 50px; font-weight: 500; line-height: 1;
  }
  .contact .value {
    margin-left: -44px;
    padding: 0 14px 0 62px;
    height: 70px;
    background: var(--ink); color: var(--white);
    font-size: 54px; line-height: 70px;
    white-space: nowrap;
  }
  .tagline {
    position: absolute; right: 22px; top: 522px;
    text-align: right;
    color: var(--purple-text);
    font-size: 50px; line-height: 60px;
  }
  .license {
    position: absolute; right: 22px; top: 658px;
    font-size: 18px; font-weight: 500; color: var(--ink);
  }
  .license .bre { color: var(--purple-text); margin-left: 8px; }
</style>
</head>
<body>
<div class="card">
  <div class="house-photo" role="img" aria-label="Photograph of a two-storey colonial house with dormer windows, tinted purple"></div>
  <svg class="accent-wedge" width="1200" height="702" viewBox="0 0 1200 702" aria-hidden="true">
    <polygon points="1034,0 1200,0 1200,702 708,702" fill="var(--yellow)"/>
  </svg>

  <h1 class="identity">
    <span class="name">Lorna Packett</span>
    <span class="title">Realtor</span>
  </h1>

  <ul class="contacts">
    <li class="contact"><span class="badge">P</span><span class="value">(555) 418-6032</span></li>
    <li class="contact"><span class="badge">@</span><span class="value">lpackett@mailbrook.example</span></li>
    <li class="contact"><span class="badge">W</span><span class="value">lornaplaces.example</span></li>
  </ul>

  <p class="tagline">Where Every Doorstep<br>Feels Familiar</p>
  <p class="license">Exp. 8/15<span class="bre">BRE #04782915</span></p>
</div>
</body>
</html>
```